Lunaform website scandinavian interior design

Existing website: http://lunaform-example.no/

Webdesign for interior designer Ragna Tveitmo. The company name is Lunaform. Scandinavian interiør is known to be simple and elegant. The website will be in Norwegian, we are working on the text. The website needs to have a few more pages than just the front page. Here are the different titles of the pages:

1. Hjem
2. Om Lunaform
3. Tjenester og priser
4.. Kontakt oss

There should be Chatterloop and Pixelane icons somewhere at the bottom of the website.

The logo we want to use is attached (pink with black print, see attachment )

We have attached images for inspiration. We want to use some of these colors. The color in the logo, The style should be elegant, modern and delicate.

It is imprtant that the website is user friendly.

Target Market(s)

People who want to decorate their home
Companies and public sector who need to redecorate

Industry/Entity Type

Interior Designer

Coding

Coded - Design and coding required

Number of Pages Required

5+ page

Font styles to use
Other font styles liked:
• see example in the logo breakdown

Requirements
Must have
• Elegant, modern and delicate design
Images of design, see examples attached
Colors similar to the pictures
Should not have
• Too bright colors
Pictures of people

```html
<!DOCTYPE html>
<html lang="no">
<head>
<meta charset="utf-8">
<title>Lunaform – Farge &amp; interiørdesign</title>
<link rel="stylesheet" href="https://fonts.googleapis.com/css2?family=Tinos&family=Poppins:wght@300;400&display=swap">
<style>
:root{
  --blush:#f3d7d6;
  --cocoa:#3b1a17;
  --ink:#2a1210;
  --muted:#8a7f7d;
  --sage:#8aa59e;
  --line:#ecd6d2;
  --white:#ffffff;
}
*{margin:0;padding:0;box-sizing:border-box}
html,body{width:1200px;height:2400px;overflow:hidden;background:var(--white)}
body{position:relative;font-family:'Poppins',sans-serif;color:var(--ink)}
.abs{position:absolute}
.serif{font-family:'Tinos',serif}

/* hero */
.hero{left:0;top:0;width:1200px;height:675px;background:linear-gradient(100deg,#c9cdd0 0%,#9aa6ab 35%,#6f7f86 65%,#4d5c62 100%)}
.hero-shade{left:0;top:0;width:1200px;height:675px;background:rgba(40,50,55,.25)}
.brand{left:161px;top:0;width:165px;height:135px}
.brand-name{left:161px;top:40px;width:165px;text-align:center;font-family:'Tinos',serif;font-size:30px;color:var(--cocoa)}
.brand-tag{left:161px;top:90px;width:165px;text-align:center;font-family:'Tinos',serif;font-size:7px;letter-spacing:1.5px;color:var(--cocoa)}
.nav{top:41px;font-family:'Tinos',serif;font-size:13px;color:var(--white);text-transform:uppercase}
.hero-title{left:0;top:232px;width:1200px;text-align:center;font-family:'Tinos',serif;font-size:54px;line-height:64px;color:var(--white)}
.btn{display:flex;align-items:center;justify-content:center;font-family:'Tinos',serif;font-size:12px;letter-spacing:2px;text-transform:uppercase}
.btn-blush{left:516px;top:387px;width:168px;height:48px;background:var(--blush);color:var(--cocoa)}

/* services */
.section-title{font-family:'Tinos',serif;font-size:32px;color:var(--cocoa);text-transform:uppercase}
.services-title{left:0;top:737px;width:1200px;text-align:center}
.service-photo{top:817px;width:390px;height:391px}
.service-name{top:1235px;width:390px;text-align:center;font-family:'Tinos',serif;font-size:13px;color:var(--cocoa)}
.service-more{top:1264px;width:390px;text-align:center;font-size:11px;letter-spacing:1px;color:var(--muted)}

/* welcome */
.welcome-panel{left:0;top:1358px;width:495px;height:495px;background:var(--blush)}
.welcome-photo{left:495px;top:1358px;width:705px;height:495px;background:linear-gradient(160deg,#8b7d72 0%,#6b5d52 40%,#b08a63 65%,#4d4844 100%)}
.welcome-title{left:163px;top:1428px;line-height:38px}
.welcome-text{left:163px;top:1522px;width:280px;font-size:12.5px;line-height:21px;color:var(--muted);font-weight:300}
.btn-cocoa{background:var(--cocoa);color:var(--white)}
.welcome-btn{left:161px;top:1716px;width:135px;height:48px}

/* contact */
.contact-title{left:163px;top:1922px}
.query-title{left:496px;top:1922px}
.contact-name{left:161px;top:2012px;width:125px;text-align:center;font-family:'Tinos',serif;font-size:30px;color:var(--cocoa)}
.contact-tag{left:161px;top:2070px;width:125px;text-align:center;font-family:'Tinos',serif;font-size:6px;letter-spacing:1.2px;color:var(--cocoa)}
.contact-row{left:161px;font-size:11px;color:var(--ink);display:flex;align-items:center;gap:10px}
.social{top:2181px;width:34px;height:33px;display:flex;align-items:center;justify-content:center;font-family:'Tinos',serif;font-size:13px}
.social-light{left:161px;background:var(--blush);color:var(--cocoa)}
.social-dark{left:206px;background:var(--cocoa);color:var(--white)}
.field-label{font-size:11px;color:var(--muted)}
.field-line{height:1px;background:var(--line)}
.send-btn{left:495px;top:2187px;width:173px;height:49px}

/* footer */
.footer{left:0;top:2311px;width:1200px;height:89px;background:var(--sage)}
.foot-link{top:2345px;font-family:'Tinos',serif;font-size:12px;color:var(--white);text-transform:uppercase}
.copyright{left:809px;top:2345px;width:228px;text-align:right;font-size:10.5px;color:var(--white)}
</style>
</head>
<body>

<header>
  <div class="abs hero" role="img" aria-label="Foto av moderne kontorlandskap med glassvegger, hvit dekorvegg og gul lenestol"></div>
  <div class="abs hero-shade"></div>
  <svg class="abs brand" viewBox="0 0 165 135" aria-hidden="true"><polygon points="0,0 165,0 165,110 82,135 0,110" fill="#f3d7d6"/></svg>
  <div class="abs brand-name">Lunaform</div>
  <div class="abs brand-tag">FARGE &amp; INTERIØRDESIGN</div>
  <nav>
    <span class="abs nav" style="left:572px">Hjem</span>
    <span class="abs nav" style="left:652px">Om Lunaform</span>
    <span class="abs nav" style="left:773px">Tjenester og priser</span>
    <span class="abs nav" style="left:951px">Kontakt oss</span>
  </nav>
  <h1 class="abs hero-title" style="font-weight:400">Trenger du hjelp til utvikling<br>av interiørmiljøer?</h1>
  <div class="abs btn btn-blush">Kontakt oss</div>
</header>

<section>
  <h2 class="abs section-title services-title" style="font-weight:400">Tjenester og priser</h2>
  <div class="abs service-photo" style="left:0;background:linear-gradient(150deg,#3c4452 0%,#b9c0cc 45%,#e8ebf0 75%,#cfd3da 100%)" role="img" aria-label="Foto av lys resepsjon med marmorgulv og hengelamper"></div>
  <div class="abs service-photo" style="left:405px;background:linear-gradient(160deg,#f5ecd8 0%,#e8c98f 40%,#a8743d 70%,#2f4a52 100%)" role="img" aria-label="Foto av møterom med rundt bord, laptop og stoler i motlys"></div>
  <div class="abs service-photo" style="left:810px;background:linear-gradient(150deg,#d8dadd 0%,#eceef0 45%,#6f8a5a 60%,#dcdcdc 100%)" role="img" aria-label="Foto av grønn plante i vase på hvit hylle"></div>
  <div class="abs service-name" style="left:0">PRIVATE INTERIØR</div>
  <div class="abs service-more" style="left:-8px">LES MER</div>
  <div class="abs service-name" style="left:405px">BEDRIFT/OFFENTLIG</div>
  <div class="abs service-more" style="left:405px">LES MER</div>
  <div class="abs service-name" style="left:810px">LEVERANDØRER</div>
  <div class="abs service-more" style="left:810px">LES MER</div>
</section>

<section>
  <div class="abs welcome-panel"></div>
  <div class="abs welcome-photo" role="img" aria-label="Foto av resepsjonsdisk i tre med oransje stoler og reoler"></div>
  <h2 class="abs section-title welcome-title" style="font-weight:400">Velkommen til<br>Lunaform</h2>
  <p class="abs welcome-text">Firma Lunaform AS jobber med utvikling av interiørmiljøer for private, bedrifter og offentlige institusjoner. For å finne de optimale løsninger til et prosjekt, enten det er et rom eller fler, kreves det kjennskap og kunnskap i markedet. Ved å bruke profesjonell kompetanse på området, sparer du både tid og penger.</p>
  <div class="abs btn btn-cocoa welcome-btn">Les mer</div>
</section>

<section>
  <h2 class="abs section-title contact-title" style="font-weight:400">Kontakt oss</h2>
  <div class="abs contact-name">Lunaform</div>
  <div class="abs contact-tag">FARGE &amp; INTERIØRDESIGN</div>
  <div class="abs contact-row" style="top:2101px">
    <svg width="12" height="12" viewBox="0 0 24 24"><path fill="#3b1a17" d="M6.6 10.8a15 15 0 0 0 6.6 6.6l2.2-2.2c.3-.3.7-.4 1-.2 1.1.4 2.3.6 3.6.6.6 0 1 .4 1 1V20c0 .6-.4 1-1 1A17 17 0 0 1 3 4c0-.6.4-1 1-1h3.5c.6 0 1 .4 1 1 0 1.3.2 2.5.6 3.6.1.3 0 .7-.2 1z"/></svg>
    <span>+4791234567</span>
  </div>
  <div class="abs contact-row" style="top:2128px">
    <svg width="12" height="10" viewBox="0 0 24 18"><rect width="24" height="18" rx="2" fill="#3b1a17"/><path d="M1 2l11 8 11-8" stroke="#fff" stroke-width="2" fill="none"/></svg>
    <span>post@lunaform-example.no</span>
  </div>
  <div class="abs social social-light" aria-label="Chatterloop">C</div>
  <div class="abs social social-dark" aria-label="Pixelane">P</div>

  <h2 class="abs section-title query-title" style="font-weight:400">For query?</h2>
  <div class="abs field-label" style="left:496px;top:1986px">Navn</div>
  <div class="abs field-label" style="left:721px;top:1986px">Kontaktnummer.</div>
  <div class="abs field-line" style="left:495px;top:2015px;width:257px"></div>
  <div class="abs field-line" style="left:772px;top:2015px;width:257px"></div>
  <div class="abs field-label" style="left:496px;top:2039px">e-post</div>
  <div class="abs field-line" style="left:495px;top:2067px;width:534px"></div>
  <div class="abs field-label" style="left:496px;top:2091px">Beskjed</div>
  <div class="abs field-line" style="left:495px;top:2172px;width:534px"></div>
  <div class="abs btn btn-cocoa send-btn">Sende melding</div>
</section>

<footer>
  <div class="abs footer"></div>
  <span class="abs foot-link" style="left:163px">Hjem</span>
  <span class="abs foot-link" style="left:228px">Om Lunaform</span>
  <span class="abs foot-link" style="left:334px">Tjenester og priser</span>
  <span class="abs foot-link" style="left:497px">Kontakt oss</span>
  <span class="abs copyright">© Lunaform - 2020. Alle rettigheter reservert.</span>
</footer>

</body>
</html>
```